VelgoNexus PowerPoint Design

We need a very cool power-point template done for VelgoNexus. We need it to drive the message of technology, speed and innovation. This is for a racing proposal to for our indy car team. I will attach our logo.

Target Market(s)

This presentation is for our INDY RACE CAR TEAM OVERVIEW... The Theme is: Speed, Technology and Innovation

Industry/Entity Type

Racing

Colors

Designer to choose colors to be used in the design.

Requirements
Must have
• Intro Slide with Logo - Must look very cool
Template Slide for Content
Ending Slide with something like "Thanks VelgoNexus!"
Nice to have
• Please see the example ppt deck from Morbeck a previous company to see the slide template... Also see a old template for VelgoNexus

```html
<!DOCTYPE html>
<html lang="en">
<head>
<meta charset="utf-8">
<title>VelgoNexus Indy Race Team Presentation Template</title>
<link href="https://fonts.googleapis.com/css2?family=Carlito:wght@400;700&display=swap" rel="stylesheet">
<style>
  :root {
    --canvas: #000000;
    --navy: #07174a;
    --navy-deep: #041038;
    --title-blue: #3a8fd0;
    --heading-blue: #1467b8;
    --body-grey: #4a4a4a;
    --bullet-green: #7aa82a;
    --badge-green: #1aa14a;
    --accent-lime: #a6c93a;
    --logo-blue: #2f8fd6;
    --white: #ffffff;
    --frame: #e8e8e8;
  }
  * { margin: 0; padding: 0; box-sizing: border-box; }
  html, body { width: 1055px; height: 1200px; overflow: hidden; background: var(--canvas); }
  body { position: relative; font-family: "Carlito", "Calibri", sans-serif; }

  .slide {
    position: absolute; width: 509px; height: 382px;
    border: 2px solid var(--frame); overflow: hidden; background: var(--white);
  }
  .slide--cover { left: 10px; top: 11px; }
  .slide--list { left: 528px; top: 11px; }
  .slide--media { left: 10px; top: 403px; }
  .slide--closing { left: 528px; top: 403px; }
  .slide--nested { left: 10px; top: 798px; }

  .lightfield {
    background:
      radial-gradient(ellipse 14px 7px at 12% 16%, rgba(95,227,224,.85), transparent 100%),
      radial-gradient(ellipse 12px 7px at 26% 12%, rgba(95,227,224,.8), transparent 100%),
      radial-gradient(ellipse 11px 7px at 72% 22%, rgba(95,227,224,.8), transparent 100%),
      radial-gradient(ellipse 10px 6px at 92% 18%, rgba(95,227,224,.8), transparent 100%),
      radial-gradient(ellipse 60% 30% at 50% 8%, rgba(31,95,184,.55), transparent 100%),
      radial-gradient(ellipse 40% 20% at 85% 12%, rgba(29,156,140,.4), transparent 100%),
      radial-gradient(ellipse 40% 22% at 15% 10%, rgba(29,156,140,.35), transparent 100%),
      linear-gradient(180deg, #0a2160 0%, var(--navy) 45%, var(--navy-deep) 100%);
  }
  .band {
    background:
      radial-gradient(ellipse 30% 80% at 20% 40%, rgba(31,95,184,.6), transparent 100%),
      radial-gradient(ellipse 25% 70% at 55% 50%, rgba(29,156,140,.45), transparent 100%),
      radial-gradient(ellipse 30% 80% at 85% 30%, rgba(31,95,184,.55), transparent 100%),
      linear-gradient(180deg, #0b2366, var(--navy));
  }

  .slide-header {
    position: absolute; left: 0; top: 0; width: 100%; height: 45px;
    border-bottom: 2px solid #1b8ea0;
  }
  .slide-title {
    position: absolute; left: 27px; top: 10px;
    color: var(--white); font-weight: 700; font-size: 20px; letter-spacing: .2px;
  }
  .slide-number {
    position: absolute; right: 11px; top: 2px; width: 22px; height: 22px;
    background: var(--badge-green); color: var(--white);
    font-weight: 700; font-size: 12px; line-height: 22px; text-align: center;
  }

  .slide-footer { position: absolute; left: 0; bottom: 0; width: 100%; height: 40px; }
  .copyright { position: absolute; left: 11px; top: 13px; color: var(--white); font-size: 10px; }
  .footer-brand {
    position: absolute; right: 12px; top: 11px;
    color: var(--logo-blue); font-size: 13px; font-weight: 700;
    display: flex; align-items: center; gap: 4px;
  }
  .brand-dot { display: inline-block; border-radius: 50%; background: var(--accent-lime); }
  .footer-brand .brand-dot { width: 6px; height: 6px; }

  .point {
    position: absolute; left: 38px; color: var(--heading-blue);
    font-weight: 700; font-size: 12px; white-space: nowrap;
    display: flex; align-items: center; gap: 6px;
  }
  .point::before {
    content: ""; width: 6px; height: 8px; flex: none;
    background:
      linear-gradient(var(--bullet-green), var(--bullet-green)) 0 0 / 2px 2px no-repeat,
      linear-gradient(var(--bullet-green), var(--bullet-green)) 0 3px / 2px 2px no-repeat,
      linear-gradient(var(--bullet-green), var(--bullet-green)) 0 6px / 2px 2px no-repeat,
      linear-gradient(var(--bullet-green), var(--bullet-green)) 3px 3px / 2px 2px no-repeat;
  }
  .subpoint {
    position: absolute; left: 47px; color: var(--body-grey); font-size: 10.8px; white-space: nowrap;
    display: flex; align-items: center; gap: 5px;
  }
  .subpoint::before {
    content: ""; width: 5px; height: 5px; flex: none;
    background:
      linear-gradient(var(--bullet-green), var(--bullet-green)) 0 0 / 2px 2px no-repeat,
      linear-gradient(var(--bullet-green), var(--bullet-green)) 3px 0 / 2px 2px no-repeat,
      linear-gradient(var(--bullet-green), var(--bullet-green)) 0 3px / 2px 2px no-repeat,
      linear-gradient(var(--bullet-green), var(--bullet-green)) 3px 3px / 2px 2px no-repeat;
  }

  .copy {
    position: absolute; left: 46px; width: 336px;
    color: var(--body-grey); font-size: 7.4px; line-height: 12.2px;
  }
  .media-tile {
    position: absolute; left: 392px; width: 84px; height: 84px;
    background: radial-gradient(circle at 50% 38%, #f2c23a 0 26%, #ff3a10 27%, #ff3300 100%);
    box-shadow: 1px 1px 3px rgba(0,0,0,.3);
  }

  .cover-brand {
    position: absolute; left: 0; top: 132px; width: 100%; text-align: center;
    color: var(--logo-blue); font-weight: 700; font-size: 24px;
    display: flex; justify-content: center; align-items: center; gap: 7px;
  }
  .cover-brand .brand-dot { width: 8px; height: 8px; }
  .cover-title {
    position: absolute; left: 104px; top: 200px; width: 326px; height: 33px;
    border-top: 1px solid rgba(58,143,208,.45); border-bottom: 1px solid rgba(58,143,208,.45);
    color: var(--title-blue); font-size: 19.5px; font-weight: 400;
    text-align: center; line-height: 33px; letter-spacing: .4px;
  }
  .cover-subtitle {
    position: absolute; left: 0; top: 242px; width: 100%; text-align: center;
    color: var(--accent-lime); font-size: 10px; letter-spacing: 2px;
  }
  .cover-copyright { position: absolute; left: 11px; bottom: 8px; color: var(--white); font-size: 8px; }

  .closing-brand { position: absolute; left: 0; top: 170px; width: 100%; text-align: center; }
  .closing-brand .brand-name {
    color: var(--logo-blue); font-weight: 700; font-size: 30px; line-height: 32px;
    display: inline-flex; align-items: center; gap: 8px;
  }
  .closing-brand .brand-dot { width: 9px; height: 9px; }
  .closing-brand .tagline { color: var(--logo-blue); font-size: 9px; margin-top: 1px; }
  .closing-message {
    position: absolute; left: 100px; top: 232px; width: 309px; height: 90px;
    border-top: 1px solid rgba(58,143,208,.3); border-bottom: 1px solid rgba(58,143,208,.3);
    color: var(--accent-lime); font-size: 19.5px; line-height: 25px; text-align: center; padding-top: 19px;
  }
  .closing-copyright { position: absolute; left: 11px; bottom: 6px; color: var(--white); font-size: 8px; }
</style>
</head>
<body>

<section class="slide slide--cover lightfield">
  <div class="cover-brand"><span class="brand-dot"></span>VelgoNexus</div>
  <h1 class="cover-title">Project Title Here</h1>
  <p class="cover-subtitle">INDY RACE CAR TEAM OVERVIEW</p>
  <p class="cover-copyright">Copyright text here</p>
</section>

<section class="slide slide--list">
  <header class="slide-header band">
    <h2 class="slide-title">Project Title Here</h2>
    <span class="slide-number">01</span>
  </header>
  <p class="point" style="top:62px">Lorem ipsum dolor sit ipsum Lorem ipsum dolor sit ipsum Lorem ipsum</p>
  <p class="point" style="top:93px">Lorem ipsum dolor sit ipsum Lorem ipsum dolor sit ipsum Lorem ipsum</p>
  <p class="point" style="top:125px">Lorem ipsum dolor sit ipsum Lorem ipsum dolor sit ipsum Lorem ipsum</p>
  <p class="point" style="top:153px">Lorem ipsum dolor sit ipsum Lorem ipsum dolor sit ipsum Lorem ipsum</p>
  <p class="point" style="top:177px">Lorem ipsum dolor sit ipsum Lorem ipsum dolor sit ipsum Lorem ipsum</p>
  <p class="point" style="top:205px">Lorem ipsum dolor sit ipsum Lorem ipsum dolor sit ipsum Lorem ipsum</p>
  <p class="point" style="top:234px">Lorem ipsum dolor sit ipsum Lorem ipsum dolor sit ipsum Lorem ipsum</p>
  <p class="point" style="top:266px">Lorem ipsum dolor sit ipsum Lorem ipsum dolor sit ipsum Lorem ipsum</p>
  <p class="point" style="top:299px">Lorem ipsum dolor sit ipsum Lorem ipsum dolor sit ipsum Lorem ipsum</p>
  <footer class="slide-footer band">
    <span class="copyright">Copyright text here</span>
    <span class="footer-brand"><span class="brand-dot"></span>VelgoNexus</span>
  </footer>
</section>

<section class="slide slide--media">
  <header class="slide-header band">
    <h2 class="slide-title">Project Title Here</h2>
    <span class="slide-number">01</span>
  </header>
  <p class="point" style="top:61px">Lorem ipsum dolor sit ipsum Lorem ipsum dolor sit ipsum Lorem ipsum</p>
  <p class="copy" style="top:86px">Lorem ipsum dolor sit ipsum Lorem ipsum dolor sit ipsum Lorem ipsum Lorem ipsum dolor sit ipsum Lorem ipsum dolor sit ipsum Lorem ipsum Lorem ipsum dolor sit ipsum Lorem ipsum dolor sit ipsum Lorem ipsum Lorem ipsum dolor sit ipsum Lorem ipsum dolor sit ipsum Lorem ipsum Lorem ipsum dolor sit ipsum Lorem ipsum dolor sit ipsum Lorem ipsum Lorem ipsum dolor sit ipsum Lorem ipsum dolor sit ipsum Lorem ipsum Lorem ipsum dolor sit ipsum Lorem ipsum dolor sit ipsum Lorem ipsum Lorem ipsum dolor sit ipsum Lorem ipsum dolor sit ipsum.</p>
  <div class="media-tile" style="top:86px" role="img" aria-label="Happy smiling face graphic on an orange tile"></div>
  <p class="point" style="top:201px">Lorem ipsum dolor sit ipsum Lorem ipsum dolor sit ipsum Lorem ipsum</p>
  <p class="copy" style="top:226px">Lorem ipsum dolor sit ipsum Lorem ipsum dolor sit ipsum Lorem ipsum Lorem ipsum dolor sit ipsum Lorem ipsum dolor sit ipsum Lorem ipsum Lorem ipsum dolor sit ipsum Lorem ipsum dolor sit ipsum Lorem ipsum Lorem ipsum dolor sit ipsum Lorem ipsum dolor sit ipsum Lorem ipsum Lorem ipsum dolor sit ipsum Lorem ipsum dolor sit ipsum Lorem ipsum Lorem ipsum dolor sit ipsum Lorem ipsum dolor sit ipsum Lorem ipsum Lorem ipsum dolor sit ipsum Lorem ipsum dolor sit ipsum Lorem ipsum Lorem ipsum dolor sit ipsum Lorem ipsum dolor sit ipsum.</p>
  <div class="media-tile" style="top:226px" role="img" aria-label="Happy smiling face graphic on an orange tile"></div>
  <footer class="slide-footer band">
    <span class="copyright">Copyright text here</span>
    <span class="footer-brand"><span class="brand-dot"></span>VelgoNexus</span>
  </footer>
</section>

<section class="slide slide--closing lightfield">
  <div class="closing-brand">
    <div class="brand-name"><span class="brand-dot"></span>VelgoNexus</div>
    <div class="tagline">Speed, Technology and Innovation</div>
  </div>
  <p class="closing-message">THANKS FOR YOUR<br>VALUABLE TIME</p>
  <p class="closing-copyright">Copyright text here</p>
</section>

<section class="slide slide--nested">
  <header class="slide-header band">
    <h2 class="slide-title">Project Title Here</h2>
    <span class="slide-number">01</span>
  </header>
  <p class="point" style="top:62px">Lorem ipsum dolor sit ipsum Lorem ipsum dolor sit ipsum Lorem ipsum</p>
  <p class="subpoint" style="top:86px">Lorem ipsum dolor sit ipsum Lorem ipsum dolor sit ipsum Lorem ipsum</p>
  <p class="subpoint" style="top:107px">Lorem ipsum dolor sit ipsum Lorem ipsum dolor sit ipsum Lorem ipsum</p>
  <p class="subpoint" style="top:126px">Lorem ipsum dolor sit ipsum Lorem ipsum dolor sit ipsum Lorem ipsum</p>
  <p class="subpoint" style="top:147px">Lorem ipsum dolor sit ipsum Lorem ipsum dolor sit ipsum Lorem ipsum</p>
  <p class="subpoint" style="top:169px">Lorem ipsum dolor sit ipsum Lorem ipsum dolor sit ipsum Lorem ipsum</p>
  <p class="point" style="top:202px">Lorem ipsum dolor sit ipsum Lorem ipsum dolor sit ipsum Lorem ipsum</p>
  <p class="point" style="top:234px">Lorem ipsum dolor sit ipsum Lorem ipsum dolor sit ipsum Lorem ipsum</p>
  <p class="point" style="top:266px">Lorem ipsum dolor sit ipsum Lorem ipsum dolor sit ipsum Lorem ipsum</p>
  <p class="point" style="top:299px">Lorem ipsum dolor sit ipsum Lorem ipsum dolor sit ipsum Lorem ipsum</p>
  <footer class="slide-footer band">
    <span class="copyright">Copyright text here</span>
    <span class="footer-brand"><span class="brand-dot"></span>VelgoNexus</span>
  </footer>
</section>

</body>
</html>
```